Tallyleaf Web Design

Create Website Design for Tallyleaf. Tallyleaf is online application for collaboration team work system (task list management). More concept design for this project please find attach file ("tallyleaf website concept.pdf") . But my concept is just describe minimal features not bind design

For tallyleaf logo, i had already attach files. But i had not decided what color i chose, so it's okay if you suggest logo color for your suitable website design.
Updates

Dear All Designer,

I like brisk carousel (http://quorvanlabs.example/brisk-carousel/),
may be your concept design can adjust with this concept.
but don't worry about script for brisk carousel, my team will be handle
You just make website design to suitable with brisk carousel

but if you had own website design concept are welcome

thanks

Target Market(s)

Business Company

Industry/Entity Type

Management

```html
<!DOCTYPE html>
<html lang="en">
<head>
<meta charset="utf-8">
<title>Tallyleaf — Collaboration Solution</title>
<link rel="stylesheet" href="https://fonts.googleapis.com/css2?family=Arimo:wght@400;700&family=Fjalla+One&display=swap">
<style>
  :root {
    --teal-dark: #1e4a55;
    --leaf: #6a9c22;
    --leaf-bright: #9cc11d;
    --sky: #34a9d4;
    --ink: #333a3f;
    --rule: #a9d8ea;
    --margin-red: #f0a8b8;
    --hero-dark: #2b2d2e;
    --footer-dark: #1d1f20;
    --muted: #7a7f82;
  }
  * { margin: 0; padding: 0; box-sizing: border-box; }
  html, body { width: 776px; height: 1200px; overflow: hidden; background: #fff; }
  body { position: relative; font-family: "Arimo", Arial, sans-serif; color: var(--ink); }
  .abs { position: absolute; }

  /* Header */
  .site-header { position: absolute; left: 0; top: 0; width: 776px; height: 94px;
    background: linear-gradient(#fdfdfd, #eceeee); }
  .brand { position: absolute; left: 16px; top: 18px; display: flex; align-items: center; gap: 6px; }
  .brand-name { font-family: "Arimo", Arial, sans-serif; font-weight: 400; font-size: 46px; color: var(--teal-dark); letter-spacing: -1px; }
  .brand-dot { width: 18px; height: 18px; border-radius: 50%; background: var(--leaf); }
  .account-btn { position: absolute; top: 13px; height: 19px; border-radius: 3px; font-size: 11px; font-weight: 700;
    display: flex; align-items: center; justify-content: center; }
  .btn-login { left: 638px; width: 50px; background: var(--leaf); color: #fff; }
  .btn-signup { left: 701px; width: 58px; background: #fff; color: var(--teal-dark); border: 1px solid var(--teal-dark); }
  .main-nav { position: absolute; top: 68px; left: 270px; display: flex; }
  .main-nav a { font-size: 15px; color: var(--teal-dark); text-decoration: none; padding: 0 13px; border-left: 1px solid #d6d9da; line-height: 18px; }
  .main-nav a:first-child { border-left: none; }
  .main-nav a.current { color: var(--leaf); }
  .nav-pointer { position: absolute; left: 297px; top: 88px; width: 0; height: 0;
    border-left: 5px solid transparent; border-right: 5px solid transparent; border-bottom: 6px solid #555; }

  /* Hero */
  .hero { position: absolute; left: 0; top: 94px; width: 776px; height: 336px;
    background: linear-gradient(160deg, #5b5e60 0%, #3a3c3d 45%, #232425 100%); }
  .hero-band { position: absolute; left: 0; top: 430px; width: 776px; height: 5px;
    background: linear-gradient(90deg, var(--leaf) 0 9%, #2a7d8f 9% 47%, var(--leaf) 47% 85%, #2a7d8f 85%); }
  .video-frame { position: absolute; left: 38px; top: 132px; width: 360px; height: 259px; background: var(--leaf-bright); }
  .video-frame::after { content: ""; position: absolute; right: 0; top: 0; border-top: 18px solid var(--hero-dark); border-left: 18px solid transparent; }
  .video-still { position: absolute; left: 20px; top: 20px; width: 319px; height: 218px; border: 1px solid #fff;
    background: linear-gradient(150deg, #4a5a66, #26323a 60%, #1c2328); }
  .play-btn { position: absolute; left: 180px; top: 225px; width: 60px; height: 60px; border-radius: 50%;
    background: var(--leaf); border: 3px solid #fff; }
  .play-btn svg { position: absolute; left: 20px; top: 15px; }
  .headline { position: absolute; left: 428px; top: 126px; font-family: "Fjalla One", "Arial Narrow", sans-serif; font-size: 37px; line-height: 45px; color: #fff; }
  .headline .accent { color: var(--leaf-bright); display: block; }
  .pricing-line { position: absolute; left: 428px; top: 232px; font-size: 14.5px; font-weight: 700; color: var(--sky); }
  .cta-tag { position: absolute; left: 436px; height: 22px; background: var(--leaf); color: #fff; padding: 0 5px;
    font-family: "Fjalla One", "Arial Narrow", sans-serif; font-size: 19px; line-height: 22px; }

  /* Welcome notebook */
  .notebook-lines { position: absolute; left: 16px; top: 489px; width: 742px; height: 241px;
    background: repeating-linear-gradient(to bottom, var(--rule) 0 1px, transparent 1px 17px); }
  .notebook-margin { position: absolute; left: 74px; top: 448px; width: 1px; height: 290px; background: var(--margin-red); }
  .welcome-title { position: absolute; left: 98px; top: 458px; font-size: 18px; color: #666; }
  .welcome-title b { color: var(--teal-dark); }
  .welcome-copy { position: absolute; left: 98px; width: 644px; font-size: 10.6px; line-height: 17px; color: var(--ink); }
  .more-arrow { position: absolute; left: 732px; top: 714px; }

  /* Feature cards */
  .card { position: absolute; top: 772px; width: 230px; height: 176px; box-shadow: 0 8px 8px -6px rgba(0,0,0,.3); }
  .card-head { position: absolute; left: 0; top: 0; width: 100%; height: 35px; color: #fff; font-size: 15px; font-weight: 700;
    display: flex; align-items: center; }
  .card-head::after { content: ""; position: absolute; right: 0; top: 0; border-top: 18px solid #fff; border-left: 18px solid transparent; opacity: 0; }
  .card-toggle { width: 29px; height: 35px; background: #111; color: #fff; font-size: 22px; display: flex; align-items: center; justify-content: center; margin-right: 8px; }
  .card-fold { position: absolute; right: 0; top: 0; width: 0; height: 0; border-left: 18px solid transparent; border-bottom: 18px solid #1b3b42; }
  .card-green { left: 16px; background: var(--leaf); }
  .card-green .card-head { background: var(--leaf); }
  .card-green .card-fold { border-bottom-color: #3e6614; }
  .card-body-text { position: absolute; left: 14px; top: 44px; width: 202px; font-size: 9.6px; font-weight: 700; line-height: 15px; text-align: justify; color: #1c2a10; }
  .card-link { position: absolute; right: 0; bottom: 0; width: 28px; height: 30px; background: #111; }
  .card-photo { left: 0; }
  .card-teal { background: #fff; border: 1px solid #ddd; }
  .card-teal .card-head { background: var(--teal-dark); }
  .card-image { position: absolute; left: 3px; top: 38px; width: 223px; height: 135px; }

  /* Footer */
  .site-footer { position: absolute; left: 0; top: 996px; width: 776px; height: 162px;
    background: linear-gradient(180deg, #2e3031, var(--footer-dark)); }
  .footer-col { position: absolute; top: 0; height: 162px; }
  .footer-divider { position: absolute; top: 0; width: 2px; height: 162px; background: #111; }
  .footer-col h3 { position: absolute; top: 8px; font-size: 15px; color: var(--sky); font-weight: 700; white-space: nowrap; }
  .footer-col ul { position: absolute; top: 38px; list-style: none; }
  .footer-col li { font-size: 9.6px; color: #e6e6e6; line-height: 19.4px; white-space: nowrap; padding-left: 16px; position: relative; }
  .footer-col li::before { content: ""; position: absolute; left: 0; top: 6px; width: 6px; height: 6px; border: 1.5px solid #bbb; border-radius: 50%; }
  .footer-col li.current { color: var(--leaf-bright); }
  .footer-col li.current::before { border-color: var(--leaf-bright); }
  .social li { padding-left: 25px; line-height: 23.6px; }
  .social li::before { top: 3px; width: 17px; height: 17px; border: none; background: #596a86; }
  .social li.mail::before { background: #888; }
  .copyright { position: absolute; left: 0; top: 1164px; width: 776px; display: flex; justify-content: center; align-items: baseline; gap: 4px; }
  .copyright small { font-size: 8.5px; color: var(--muted); }
  .copyright span { font-size: 17px; color: var(--teal-dark); }
</style>
</head>
<body>

<header class="site-header">
  <div class="brand"><span class="brand-name">tallyleaf</span><span class="brand-dot"></span></div>
  <a class="account-btn btn-login">Login</a>
  <a class="account-btn btn-signup">Singup</a>
  <nav class="main-nav">
    <a class="current">Home</a><a>About Us</a><a>Tour</a><a>Pricing</a><a>Costomers</a><a>Contact Us</a>
  </nav>
  <span class="nav-pointer"></span>
</header>

<section class="hero" role="img" aria-label="Busy city crowd photo in dark grey tones"></section>
<div class="hero-band"></div>
<div class="video-frame">
  <div class="video-still" role="img" aria-label="Product video still: notebook on a desk beside a globe"></div>
  <div class="play-btn" style="left:140px;top:93px;"><svg width="22" height="26" viewBox="0 0 22 26"><path d="M2 1 L21 13 L2 25 Z" fill="#fff"/></svg></div>
</div>
<h1 class="headline">The most complete<span class="accent">collaboration solution</span></h1>
<p class="pricing-line">Free up to 5 users · Pro from $5/mo per user</p>
<span class="cta-tag" style="top:332px;">GET STARTED WITH</span>
<span class="cta-tag" style="top:366px;">A FREE VERSION OF TALLYLEAF</span>

<section>
  <div class="notebook-lines"></div>
  <div class="notebook-margin"></div>
  <h2 class="welcome-title">Welcome <b>Tallyleaf!</b></h2>
  <p class="welcome-copy" style="top:490px;">Lorem ipsum dolor sit amet, consectetur adipiscing elit. Vestibulum accumsan, diam pulvinar fermentum vestibulum, enim felis mollis quam, quis aliquet nisl justo sed neque. Suspendisse potenti. Praesent sed nunc lorem. Class aptent taciti sociosqu ad litora torquent per conubia nostra, per inceptos himenaeos. In vestibulum luctus est non commodo. Donec consectetur urna non magna cursus eget lobortis est egestas. Cras pellentesque leo non est tincidunt quis tempus neque vulputate. Curabitur vitae eros arcu, at luctus metus. Class aptent taciti sociosqu ad litora torquent per conubia nostra, per inceptos himenaeos. Vestibulum tellus nisl, convallis nec elementum nec, tempor eu elit. Morbi mauris libero, iaculis dapibus faucibus ac, scelerisque vel nulla. Phasellus pellentesque blandit sapien eget consectetur</p>
  <p class="welcome-copy" style="top:626px;">Lorem ipsum dolor sit amet, consectetur adipiscing elit. Vestibulum accumsan, diam pulvinar fermentum vestibulum, enim felis mollis quam, quis aliquet nisl justo sed neque. Suspendisse potenti. Praesent sed nunc lorem. Class aptent taciti sociosqu ad litora torquent per conubia nostra, per inceptos himenaeos. In vestibulum luctus est non commodo. Donec consectetur urna non magna cursus eget lobortis est egestas. Cras pellentesque leo non est tincidunt quis tempus neque vulputate. Curabitur vitae eros arcu, at luctus metus.</p>
  <svg class="more-arrow" width="10" height="14" viewBox="0 0 10 14"><path d="M2 1 L8 7 L2 13" fill="none" stroke="var(--leaf)" stroke-width="3"/></svg>
</section>

<article class="card card-green">
  <div class="card-head"><span class="card-toggle">-</span>Customize Application<span class="card-fold"></span></div>
  <p class="card-body-text">Lorem ipsum dolor sit amet, consectetur adipiscing elit. Vestibulum accumsan, diam pulvinar fermentum vestibulum, enim felis mollis quam, quis aliquet nisl justo sed neque. Suspendisse potenti. Praesent sed nunc lorem. Class aptent taciti sociosqu.</p>
  <div class="card-link"><svg width="28" height="30" viewBox="0 0 28 30"><g fill="none" stroke="#fff" stroke-width="2.2"><rect x="7" y="13" width="9" height="6" rx="3" transform="rotate(-45 11 16)"/><rect x="12" y="9" width="9" height="6" rx="3" transform="rotate(-45 16 12)"/></g></svg></div>
</article>

<article class="card card-teal" style="left:273px;">
  <div class="card-head"><span class="card-toggle">+</span>Synchronize All Device<span class="card-fold"></span></div>
  <div class="card-image" role="img" aria-label="Connected devices network illustration" style="background:radial-gradient(circle at 50% 45%, #f4f6f7, #b8bcbe 70%, #8e9294);"></div>
</article>

<article class="card card-teal" style="left:530px;">
  <div class="card-head" style="justify-content:center;"><span class="card-toggle" style="position:absolute;left:0;top:0;">+</span>Report<span class="card-fold"></span></div>
  <div class="card-image" role="img" aria-label="Business report documents and pens photo" style="background:linear-gradient(135deg, #3b3f44, #9a9fa6 55%, #e3e4e6);"></div>
</article>

<footer class="site-footer">
  <div class="footer-divider" style="left:117px;"></div>
  <div class="footer-divider" style="left:301px;"></div>
  <div class="footer-divider" style="left:473px;"></div>
  <div class="footer-divider" style="left:645px;"></div>
  <div class="footer-col" style="left:15px;"><h3>Site Links</h3>
    <ul><li class="current">Home</li><li>About Us</li><li>Tour</li><li>Pricing</li><li>Costomers</li><li>Contact Us</li></ul></div>
  <div class="footer-col" style="left:171px;"><h3>Resources</h3>
    <ul><li>Blog</li><li>Support Center</li><li>F.A.Q</li><li>Developers</li><li>API Documentation</li></ul></div>
  <div class="footer-col" style="left:342px;"><h3>Products</h3>
    <ul><li>Tallyleaf Tracker</li><li>Free trial</li><li>Why Tallyleaf</li></ul></div>
  <div class="footer-col" style="left:522px;"><h3>Company</h3>
    <ul><li>Company</li><li>Leadership team</li><li>Careers</li><li>Newsletters</li><li>Contact</li></ul></div>
  <div class="footer-col" style="left:690px;"><h3>Socials</h3>
    <ul class="social" style="top:33px;"><li>Friendwall</li><li>Chirpline</li><li>Worklinkr</li><li class="mail">Mail</li></ul></div>
</footer>

<div class="copyright"><small>Copyright © 2013,</small><span>tallyleaf</span></div>

</body>
</html>
```